Infographic for Anesthesia Management Company

I would like my Anesthesia Management company, Verity Sedation, service information placed into a infographic for use on a brochure and webpage. Please focus on just the infographic.
-Verity Services text to be placed into infographic attached in word file.
-Two Vector infographic templates attached as well. I am open to either option, or alternative layout suggestion.
-Please match color scheme to veritysedation.com
-Verity logo attached.
Thank you for your help!
Todd
Target Market(s)
Surgery Centers
Industry/Entity Type
It Company
Font styles to use
Requirements
Must have
- Professional Look.
- Easy to read text.
- Cohesive branding
Nice to have
- Please see attached Vector examples.

```html
<!DOCTYPE html>
<html lang="en">
<head>
<meta charset="utf-8">
<title>Verity Sedation – Anesthesia Provider Recruitment, Credentialing, And Staffing</title>
<link rel="stylesheet" href="https://fonts.googleapis.com/css2?family=Roboto:wght@400;500;700&family=Roboto+Condensed:wght@400;700&display=swap">
<style>
  :root {
    --ink: #444449;
    --body: #2f2f33;
    --lavender: #e6e1ea;
    --mint: #d5f1ec;
    --purple: #84718f;
    --purple-fold: #a898b0;
    --teal: #1fbca2;
    --teal-fold: #6fd4c2;
    --icon-purple: #8a7895;
    --icon-teal: #22b79e;
    --white: #ffffff;
  }
  * { box-sizing: border-box; margin: 0; padding: 0; }
  html, body {
    width: 1200px; height: 814px; overflow: hidden;
    background: var(--white);
  }
  .infographic {
    position: relative;
    width: 1050px; height: 712px;
    transform: scale(1.142857);
    transform-origin: 0 0;
    font-family: "Roboto", Arial, sans-serif;
  }
  .shapes { position: absolute; inset: 0; }
  .title {
    position: absolute; left: 0; right: 0; top: 72px;
    text-align: center;
    font-size: 27.5px; font-weight: 700;
    color: var(--ink);
    letter-spacing: 0.1px;
  }
  .pillar {
    position: absolute; left: 251px; width: 215px;
    color: var(--white);
    font-family: "Roboto Condensed", "Arial Narrow", sans-serif;
  }
  .pillar-name { font-size: 16px; font-weight: 700; letter-spacing: 0.2px; line-height: 20px; }
  .pillar-role { font-size: 16.5px; font-weight: 400; line-height: 21px; margin-top: 4px; }
  .details {
    position: absolute; left: 516px; width: 420px;
    font-size: 12px; line-height: 16.6px; color: var(--body);
    list-style: none;
  }
  .details li { position: relative; padding-left: 14px; }
  .details li::before { content: "•"; position: absolute; left: 0; }
  .details .subhead {
    padding-left: 12px; font-weight: 700; margin: 4px 0 4px;
  }
  .details .subhead::before { content: none; }
</style>
</head>
<body>
<main class="infographic">
  <svg class="shapes" width="1050" height="712" viewBox="0 0 1050 712" aria-hidden="true">
    <!-- row bands -->
    <g class="band-left">
      <polygon points="52,137 215,137 215,265 52,265 96,201" fill="var(--lavender)"/>
      <polygon points="52,265 215,265 215,393 52,393 96,329" fill="var(--mint)"/>
      <polygon points="52,393 215,393 215,520 52,520 96,456" fill="var(--lavender)"/>
      <polygon points="52,520 215,520 215,648 52,648 96,584" fill="var(--mint)"/>
    </g>
    <g class="band-right">
      <polygon points="485,137 960,137 1000,201 960,265 485,265" fill="var(--lavender)"/>
      <polygon points="485,265 960,265 1000,329 960,393 485,393" fill="var(--mint)"/>
      <polygon points="485,393 960,393 1000,456 960,520 485,520" fill="var(--lavender)"/>
      <polygon points="485,520 960,520 1000,584 960,648 485,648" fill="var(--mint)"/>
    </g>
    <!-- folds -->
    <g class="folds">
      <polygon points="215,137 232,162 232,277 215,265" fill="var(--purple-fold)"/>
      <polygon points="468,162 485,137 485,265 468,277" fill="var(--purple-fold)"/>
      <polygon points="215,265 232,277 232,393 215,393" fill="var(--teal-fold)"/>
      <polygon points="468,277 485,265 485,393 468,393" fill="var(--teal-fold)"/>
      <polygon points="215,393 232,393 232,510 215,520" fill="var(--purple-fold)"/>
      <polygon points="468,393 485,393 485,520 468,510" fill="var(--purple-fold)"/>
      <polygon points="215,520 232,510 232,622 215,648" fill="var(--teal-fold)"/>
      <polygon points="468,510 485,520 485,648 468,622" fill="var(--teal-fold)"/>
    </g>
    <!-- pillar boxes -->
    <rect x="232" y="162" width="236" height="115" fill="var(--purple)"/>
    <rect x="232" y="277" width="236" height="116" fill="var(--teal)"/>
    <rect x="232" y="393" width="236" height="117" fill="var(--purple)"/>
    <rect x="232" y="510" width="236" height="112" fill="var(--teal)"/>

    <!-- icons -->
    <g class="icon-provider" fill="none" stroke="var(--icon-purple)" stroke-width="1.5" stroke-linecap="round" stroke-linejoin="round">
      <path d="M139,181 h26 v8 h-26 z"/>
      <path d="M152,183 v5 M149.5,185.5 h5"/>
      <ellipse cx="152" cy="202" rx="13" ry="14"/>
      <path d="M121,243 v-8 c0,-8 10,-13 22,-15 h18 c12,2 22,7 22,15 v8"/>
      <path d="M166,238 h8"/>
    </g>
    <g class="icon-kit" fill="none" stroke="var(--icon-teal)" stroke-width="1.5" stroke-linejoin="round">
      <rect x="124" y="317" width="62" height="44" rx="3"/>
      <path d="M145,317 v-9 h20 v9"/>
      <path d="M150,330 h10 v7 h7 v10 h-7 v7 h-10 v-7 h-7 v-10 h7 z"/>
    </g>
    <g class="icon-heart" fill="none" stroke="var(--icon-purple)" stroke-width="1.5" stroke-linejoin="round" stroke-linecap="round">
      <path d="M155,486 c-18,-14 -32,-24 -32,-40 c0,-10 8,-17 17,-17 c7,0 12,4 15,9 c3,-5 8,-9 15,-9 c9,0 17,7 17,17 c0,16 -14,26 -32,40 z"/>
      <path d="M123,458 h20 l5,-10 l6,22 l6,-16 l4,4 h23"/>
    </g>
    <g class="icon-care" fill="none" stroke="var(--icon-teal)" stroke-width="1.5" stroke-linejoin="round" stroke-linecap="round">
      <circle cx="155" cy="550" r="7"/>
      <path d="M141,578 c0,-9 6,-14 14,-14 c8,0 14,5 14,14"/>
      <path d="M124,560 v20 l12,12 v12 M132,566 v10 l8,8"/>
      <path d="M186,560 v20 l-12,12 v12 M178,566 v10 l-8,8"/>
    </g>
  </svg>

  <h1 class="title">Anesthesia Provider Recruitment, Credentialing, And Staffing</h1>

  <div class="pillar" style="top:200px">
    <p class="pillar-name">PROFESSIONALISM</p>
    <p class="pillar-role">ASC Stakeholder Satisfaction</p>
  </div>
  <div class="pillar" style="top:298px">
    <p class="pillar-name">ACCOUNTABILITY</p>
    <p class="pillar-role">Meeting Accreditation<br>Requirements</p>
  </div>
  <div class="pillar" style="top:427px">
    <p class="pillar-name">EFFICIENCY</p>
    <p class="pillar-role">Thought Leadership</p>
  </div>
  <div class="pillar" style="top:532px">
    <p class="pillar-name">PATIENT SAFETY</p>
    <p class="pillar-role">Clinical Guidance and Quality<br>Improvement</p>
  </div>

  <ul class="details" style="top:169px">
    <li>Share our personal network of highly qualified anesthesia providers</li>
    <li>Create continuity between anesthesia, surgeon, and ASC staff</li>
    <li>Guarantee every anesthesia provider upholds clinical excellence</li>
    <li>Coordinate staffing to meet your scheduled case volume</li>
  </ul>
  <ul class="details" style="top:279px">
    <li>Partner with your surgery center to ensure anesthesia policies and procedures are up to current ASC credentialing standards</li>
    <li class="subhead">In-House Billing</li>
    <li>Dedicated in-house billers ensure anesthesia billing is processed correctly the first time</li>
  </ul>
  <ul class="details" style="top:418px">
    <li>Stipend free anesthesia services</li>
    <li>Proprietary and data-driven process to maintain on-time surgery flow</li>
  </ul>
  <ul class="details" style="top:536px">
    <li>Pre-operative protocols to minimize cancellations and optimize patient outcomes</li>
    <li>Patient selection criteria to ensure suitable surgical candidates</li>
    <li>Education programs to engage the clinical staff</li>
    <li>Evidence based multimodal pain management protocol to facilitate a timely discharge and reduce patient side effects</li>
  </ul>
</main>
</body>
</html>
```